Business Card Design - Corporate

Create a sleek elegant business card layout while suggesting a color scheme. Convey cutting edge technology while maintaining a corporate feel that is easily readable.

Company designs and manufactures consumer electronic products for mass retail that are mainly app driven.

(vector logo and die-line provided)

Target Market(s)

Corporate level, tech industry.

Industry/Entity Type

Business

Contact Information for Business Card

Generic Info:

Name
Title
email
address
phone 1
phone 2
website (quillbarn.com) on back

Font styles to use
Sans Serif

Requirements
Must have
• At least 2 colors + white on one side.
Nice to have
• Solid suggestion on color for logo and overall design. Color flood on back of card.
Should not have
• background texture like... marble, stone, patterns or circuit boards

```html
<!DOCTYPE html>
<html lang="en">
<head>
<meta charset="utf-8">
<title>Quillbarn Business Card</title>
<link rel="stylesheet" href="https://fonts.googleapis.com/css2?family=Montserrat:wght@500;700&family=Open+Sans:wght@400;600&display=swap">
<style>
  :root {
    --bg: #d6e7f0;
    --brand-blue: #0a71b8;
    --ink: #222222;
    --ink-soft: #4a4a4a;
    --muted: #9a9a9a;
    --paper: #ffffff;
  }
  * { box-sizing: border-box; margin: 0; padding: 0; }
  html, body { width: 1200px; height: 1200px; overflow: hidden; }
  body {
    position: relative;
    background: var(--bg);
    font-family: "Open Sans", sans-serif;
    color: var(--ink);
  }
  .brand-mark {
    position: absolute;
    top: 78px;
    right: 70px;
    display: flex;
    align-items: center;
    gap: 14px;
  }
  .brand-mark__name {
    font-family: "Montserrat", sans-serif;
    font-weight: 500;
    font-size: 58px;
    letter-spacing: 8px;
    color: var(--ink-soft);
  }
  .brand-mark__dot {
    width: 16px; height: 16px;
    border-radius: 50%;
    background: var(--brand-blue);
  }
  .card {
    position: absolute;
    width: 600px;
    height: 343px;
    border-radius: 2px;
    box-shadow: 0 6px 18px rgba(40, 70, 90, 0.18);
  }
  .card--front {
    left: 80px;
    top: 250px;
    background: var(--brand-blue);
    display: flex;
    align-items: center;
    justify-content: center;
  }
  .card--front .wordmark {
    font-family: "Montserrat", sans-serif;
    font-weight: 500;
    font-size: 52px;
    letter-spacing: 8px;
    color: var(--paper);
  }
  .card--back {
    left: 520px;
    top: 640px;
    background: var(--paper);
    padding: 58px 0 0 62px;
  }
  .holder__name {
    font-family: "Montserrat", sans-serif;
    font-weight: 700;
    font-size: 28px;
    color: var(--ink);
    line-height: 1.1;
  }
  .holder__position {
    font-size: 18px;
    color: var(--muted);
    margin-top: 2px;
  }
  .card--back .wordmark {
    font-family: "Montserrat", sans-serif;
    font-weight: 500;
    font-size: 34px;
    letter-spacing: 5px;
    color: var(--ink-soft);
    margin-top: 34px;
  }
  .address {
    font-size: 17px;
    line-height: 1.35;
    margin-top: 12px;
    color: var(--ink);
  }
  .contacts {
    margin-top: 10px;
    display: grid;
    grid-template-columns: auto auto;
    justify-content: start;
    column-gap: 16px;
    row-gap: 4px;
    font-size: 16px;
  }
  .contact { display: flex; align-items: center; gap: 6px; white-space: nowrap; }
  .contact__icon { width: 16px; height: 16px; flex: none; }
</style>
</head>
<body>
  <header class="brand-mark">
    <span class="brand-mark__name">QUILLBARN</span>
    <span class="brand-mark__dot"></span>
  </header>

  <section class="card card--front" aria-label="Card front">
    <span class="wordmark">QUILLBARN</span>
  </section>

  <section class="card card--back" aria-label="Card back">
    <p class="holder__name">Name Here</p>
    <p class="holder__position">Position</p>
    <p class="wordmark">QUILLBARN</p>
    <p class="address">2470 Marlow St, Suite 310<br>Fairhaven, CA 94512, USA</p>
    <div class="contacts">
      <span class="contact">
        <svg class="contact__icon" viewBox="0 0 16 16" aria-hidden="true"><circle cx="8" cy="8" r="7" fill="none" stroke="#0a71b8" stroke-width="1.2"/><rect x="5.5" y="3.8" width="5" height="8.4" rx="1" fill="none" stroke="#0a71b8" stroke-width="1.1"/></svg>
        (000) 000-0000
      </span>
      <span class="contact">
        <svg class="contact__icon" viewBox="0 0 16 16" aria-hidden="true"><circle cx="8" cy="8" r="7" fill="none" stroke="#0a71b8" stroke-width="1.2"/><path d="M5 5.2c.6-.6 1.2-.5 1.5 0l.6 1c.2.4 0 .8-.3 1 .4.8 1 1.4 1.8 1.8.2-.3.6-.5 1-.3l1 .6c.5.3.6.9 0 1.5-1.6 1.5-6.9-3.6-5.6-5.6z" fill="#0a71b8"/></svg>
        (555) 214-7730
      </span>
      <span class="contact">
        <svg class="contact__icon" viewBox="0 0 16 16" aria-hidden="true"><circle cx="8" cy="8" r="7" fill="none" stroke="#0a71b8" stroke-width="1.2"/><rect x="4.3" y="5.3" width="7.4" height="5.4" rx=".6" fill="#0a71b8"/><path d="M4.5 5.6 8 8.3l3.5-2.7" fill="none" stroke="#fff" stroke-width=".8"/></svg>
        info@quillbarn.com
      </span>
      <span class="contact">
        <svg class="contact__icon" viewBox="0 0 16 16" aria-hidden="true"><circle cx="8" cy="8" r="7" fill="none" stroke="#0a71b8" stroke-width="1.2"/><circle cx="8" cy="8" r="3.8" fill="none" stroke="#0a71b8" stroke-width="1"/><path d="M4.2 8h7.6M8 4.2c-1.6 2.2-1.6 5.4 0 7.6M8 4.2c1.6 2.2 1.6 5.4 0 7.6" fill="none" stroke="#0a71b8" stroke-width=".8"/></svg>
        www.quillbarn.com
      </span>
    </div>
  </section>
</body>
</html>
```